PeppleDorven.com needs graphics of notable women of science

PeppleDorven.com is devoted to promoting education in science, technology, engineering and science for girls and women. Currently we sell t-shirts adorned with graphics and accomplishments of Tessa Volk, Opal Brindmoor and Gwen Tarrow.
Our next project is a calendar with a different woman on each month:
Opal Brindmoor
Lotte Brauns
Suvarna Meghle
Gwen Tarrow
Judith Pallow
Tessa Volk
Octavia Bellweir
Helena Dorsett
Clara J Finchley Warbeck
Zelda Brunt
Greta Olsvang
Nora Quillet
Images can be stylized monochrome like t-shirts (https://www.crafolo.com/shop/PeppleDorven) or stylized color as long as all months are the same. I can provide more information on each woman if desired.
Thank you for the designs that have been submitted so far. They have made me realize that I haven't been clear about one thing. When I said the images had to be 'stylized' I meant it can't just be a photo taken off of the internet. Many of these photos have copyright protection. If you look at the images I created for the t-shirts, the photos have been significantly changed. That is what these images will require as well.

```html
<!DOCTYPE html>
<html lang="en">
<head>
<meta charset="utf-8">
<title>Lotte Brauns – February Calendar</title>
<link href="https://fonts.googleapis.com/css2?family=Open+Sans:wght@300;400;600&display=swap" rel="stylesheet">
<style>
  :root {
    --page: #ffffff;
    --ink: #555557;
    --ink-dark: #333335;
    --title-band: #58585a;
    --cell: #e4e4e5;
    --sunday: #e8303a;
    --weekday: #6b2c91;
    --saturday: #333335;
    --portrait-light: #ececec;
    --portrait-mid: #bdbdbd;
    --portrait-dark: #7a7a7a;
  }
  * { box-sizing: border-box; margin: 0; padding: 0; }
  html, body { width: 776px; height: 1200px; overflow: hidden; background: var(--page); }
  body { position: relative; font-family: "Open Sans", Arial, sans-serif; color: var(--ink); }

  .portrait {
    position: absolute; left: 0; top: 0; width: 776px; height: 600px;
    background: radial-gradient(ellipse 260px 330px at 400px 330px, var(--portrait-mid), var(--portrait-light) 75%),
                var(--portrait-light);
  }
  .portrait-shade {
    position: absolute; left: 250px; top: 60px; width: 360px; height: 540px;
    background: radial-gradient(ellipse at 50% 30%, var(--portrait-dark), transparent 70%);
    opacity: .35;
  }

  .name-band {
    position: absolute; left: 30px; top: 500px; width: 442px; height: 100px;
    background: var(--title-band);
    display: flex; align-items: center; padding-left: 24px;
  }
  .name-band h1 { font-weight: 300; font-size: 35px; color: #fff; letter-spacing: .2px; }

  .biography {
    position: absolute; left: 53px; top: 614px; width: 672px;
    font-size: 9.2px; line-height: 10.6px; color: var(--ink);
  }
  .biography p + p { margin-top: 9px; }

  .month-panel {
    position: absolute; left: 30px; top: 910px; width: 137px; height: 132px;
    background: var(--title-band); color: #fff; text-align: center; padding-top: 36px;
  }
  .month-panel h2 { font-size: 20px; font-weight: 600; }
  .month-panel .holiday { font-size: 8.5px; margin-top: 8px; }

  .calendar {
    position: absolute; left: 183px; top: 911px;
    display: grid; grid-template-columns: repeat(7, 78px); column-gap: 3px;
    grid-template-rows: 39px repeat(5, 42px); row-gap: 4px;
  }
  .weekday {
    display: flex; align-items: center; justify-content: center;
    color: #fff; font-size: 21px; font-weight: 400;
  }
  .weekday.sun { background: var(--sunday); }
  .weekday.mid { background: var(--weekday); }
  .weekday.sat { background: var(--saturday); }
  .day {
    background: var(--cell); display: flex; align-items: flex-end; justify-content: flex-end;
    padding: 0 10px 6px 0; font-size: 16px; color: var(--ink);
  }
  .day.empty { background: transparent; }
  .day.sun, .day.holiday { color: var(--sunday); }
  .day.sat { color: var(--ink-dark); font-weight: 600; }

  .brand {
    position: absolute; left: 30px; top: 1058px;
    font-size: 20px; font-weight: 400; color: var(--ink-dark); letter-spacing: .5px;
  }
  .contacts { position: absolute; left: 30px; top: 1118px; list-style: none; }
  .contacts li {
    display: flex; align-items: center; gap: 6px;
    font-size: 10.5px; color: var(--ink); height: 18.5px;
  }
  .contacts .mark { width: 12px; height: 12px; background: var(--ink); display: block; }
  .contacts svg { width: 12px; height: 12px; display: block; }
</style>
</head>
<body>
  <div class="portrait" role="img" aria-label="Stylized black and white portrait of Lotte Brauns in a high-collared blouse with a bow">
    <div class="portrait-shade"></div>
  </div>

  <div class="name-band"><h1>Lotte Brauns</h1></div>

  <section class="biography">
    <p>Lotte Brauns - 4 October 1879 – 21 January 1951, was an inventive mathematician and astronomer known for her pioneering methods for charting the orbits of comets and for her early work on numerical tables. Colleagues described her as a patient, exacting thinker whose careful calculations set a new standard for accuracy. Her reduction method, still taught in observatories, showed how long columns of raw observations could be turned into reliable predictions of where a body would appear.</p>
    <p>She grew up in a harbour town where her mother kept the accounts of a small shipping office, and she learned arithmetic by checking tide tables at the kitchen table. Lotte first trained as a schoolteacher, but a borrowed book on celestial mechanics changed her plans. She joined a provincial observatory as an unpaid computer in 1901 and spent nine years reducing photographic plates by lamplight. In 1910 a visiting director noticed that her figures never needed correction and offered her a salaried post. Her first paper, on the return of a faint periodic comet, appeared in 1912 under her own name, a rare event for a woman at the time.</p>
    <p>Over the next two decades she led a small team of computers, most of them young women, who proudly called themselves the "night shift". Together they produced a catalogue of more than four thousand star positions and a set of tables used by navigators on three continents. She travelled widely to lecture, insisted that every assistant be credited in print, and founded a scholarship for girls who wished to study astronomy. In 1938 she was elected the first woman president of her national astronomical society, a post she held for six years.</p>
    <p>Her later work turned to the mathematics of error itself. She showed how small mistakes in timing could grow over many orbits, and she designed checking schemes that let a single computer find her own slips before they spread through a table. These ideas were adopted by mapmakers, surveyors and, later, by the first engineers who programmed electronic calculating machines. After her retirement she wrote a popular book on the night sky for young readers, which remained in print for decades and inspired many of them to pursue careers in science. In addition to her own publications, she answered hundreds of letters from students and amateur observers, and is credited with encouraging several lines of research carried out by others. A small crater on the Moon and a main-belt asteroid were later named in her honour, and the observatory where she began now awards a yearly prize in her name.</p>
  </section>

  <aside class="month-panel">
    <h2>February</h2>
    <p class="holiday">Feb 17 | Presidents' Day</p>
  </aside>

  <div class="calendar">
    <div class="weekday sun">S</div>
    <div class="weekday mid">M</div>
    <div class="weekday mid">T</div>
    <div class="weekday mid">W</div>
    <div class="weekday mid">T</div>
    <div class="weekday mid">F</div>
    <div class="weekday sat">S</div>

    <div class="day empty"></div><div class="day empty"></div><div class="day empty"></div>
    <div class="day empty"></div><div class="day empty"></div><div class="day empty"></div>
    <div class="day sat">1</div>

    <div class="day sun">2</div><div class="day">3</div><div class="day">4</div><div class="day">5</div>
    <div class="day">6</div><div class="day">7</div><div class="day sat">8</div>

    <div class="day sun">9</div><div class="day">10</div><div class="day">11</div><div class="day">12</div>
    <div class="day">13</div><div class="day">14</div><div class="day sat">15</div>

    <div class="day sun">16</div><div class="day holiday">17</div><div class="day">18</div><div class="day">19</div>
    <div class="day">20</div><div class="day">21</div><div class="day sat">22</div>

    <div class="day sun">23</div><div class="day">24</div><div class="day">25</div><div class="day">26</div>
    <div class="day">27</div><div class="day">28</div><div class="day empty"></div>
  </div>

  <div class="brand">PeppleDorven</div>

  <ul class="contacts">
    <li><span class="mark"></span>mara.keswick.4</li>
    <li><span class="mark"></span>mara@peppledorven.com</li>
    <li>
      <svg viewBox="0 0 12 12" aria-hidden="true"><rect width="12" height="12" fill="#555557"/><path d="M2 3.5h8v5H2z M2 3.5l4 3 4-3" fill="none" stroke="#fff" stroke-width="0.9"/></svg>
      @PeppleDorven
    </li>
    <li>
      <svg viewBox="0 0 12 12" aria-hidden="true"><rect width="12" height="12" fill="#555557"/><circle cx="6" cy="6" r="3.6" fill="none" stroke="#fff" stroke-width="0.8"/><path d="M2.4 6h7.2 M6 2.4c-1.8 2-1.8 5.2 0 7.2 M6 2.4c1.8 2 1.8 5.2 0 7.2" fill="none" stroke="#fff" stroke-width="0.7"/></svg>
      www.peppledorven.com
    </li>
  </ul>
</body>
</html>
```